Business Podcaster needs a sexy book cover design for upcoming book launch

I'm launching a book called Find Your Mentor: how to accelerate your growth through reaching out, getting a response from, and leaving an impression on the people you admire most. It would be cool to have maybe a band of heroes or a single hero or something on the cover, then I'll need the spine designed, as well as the back cover which would be mostly just quotes about the book from other prominent people.

I dont want to extend it. I want to shorten it. Can I do that?

```html
<!DOCTYPE html>
<html lang="en">
<head>
<meta charset="utf-8">
<title>Find Your Mentor — Book Cover Wrap</title>
<link href="https://fonts.googleapis.com/css2?family=Bebas+Neue&family=Didact+Gothic&family=Libre+Baskerville&family=Oswald:wght@600&display=swap" rel="stylesheet">
<style>
  :root {
    --paper: #ffffff;
    --royal: #003399;
    --sky: #3a63c8;
    --steel: #2f5e9c;
    --cape: #f2302f;
    --ink: #000000;
  }
  * { margin: 0; padding: 0; box-sizing: border-box; }
  html, body { width: 1200px; height: 837px; overflow: hidden; background: var(--paper); }
  .wrap { position: relative; width: 1200px; height: 837px; background: var(--paper); }
  .title-svg text { fill: var(--royal); }
  .display { font-family: "Bebas Neue", "Oswald", sans-serif; }
  .serif { font-family: "Libre Baskerville", Georgia, serif; }
  .title-svg .your { fill: var(--sky); }

  /* Back cover */
  .back-title { position: absolute; left: 80px; top: 52px; width: 370px; height: 68px; }
  .back-blurb {
    position: absolute; left: 34px; top: 142px; width: 474px;
    font-family: "Didact Gothic", "Century Gothic", sans-serif;
    font-size: 12.4px; line-height: 13.7px; color: var(--royal);
    text-align: justify; hyphens: auto;
  }
  .back-blurb p + p { margin-top: 13.7px; }
  .isbn-box { position: absolute; left: 322px; top: 643px; width: 186px; height: 121px; background: var(--royal); }

  /* Spine */
  .spine-title { position: absolute; left: 560px; top: 58px; width: 76px; height: 360px; }
  .spine-author { position: absolute; left: 572px; top: 570px; width: 50px; height: 225px; }
  .spine-author text, .front-author text { fill: var(--ink); font-family: "Oswald", "Bebas Neue", sans-serif; font-weight: 600; }

  /* Front cover */
  .front-title { position: absolute; left: 660px; top: 50px; width: 530px; height: 500px; }
  .rule { position: absolute; left: 720px; width: 405px; height: 2px;
    background: linear-gradient(90deg, transparent, var(--steel) 20%, var(--royal) 50%, var(--steel) 80%, transparent); }
  .rule--top { top: 584px; }
  .rule--bottom { top: 681px; }
  .subtitle { position: absolute; left: 690px; top: 596px; width: 465px; height: 80px; }
  .subtitle text { fill: var(--steel); font-family: "Bebas Neue", "Oswald", sans-serif; font-size: 24px; }
  .front-author { position: absolute; left: 780px; top: 738px; width: 280px; height: 56px; }
</style>
</head>
<body>
<main class="wrap">

  <!-- Back cover -->
  <section class="back-cover">
    <svg class="back-title title-svg" viewBox="0 0 370 68" aria-label="Find Your Mentor">
      <text class="display" x="4" y="62" font-size="84" textLength="112" lengthAdjust="spacingAndGlyphs">FIND</text>
      <text class="serif your" x="128" y="56" font-size="29" textLength="90" lengthAdjust="spacingAndGlyphs">YOUR</text>
      <text class="display" x="228" y="62" font-size="84" textLength="140" lengthAdjust="spacingAndGlyphs">MENTOR</text>
    </svg>
    <div class="back-blurb">
      <p>Lorem ipsum dolor sit amet, consectetur adipisicing elit, sed do eiusmod tempor incididunt ut labore et dolore magna aliqua. Ut enim ad minim veniam, quis nostrud exercitation ullamco laboris nisi ut aliquip ex ea commodo consequat. Duis aute irure dolor in reprehenderit in voluptate velit esse cillum dolore eu fugiat nulla pariatur. Excepteur sint occaecat cupidatat non proident, sunt in culpa qui officia deserunt mollit anim id est laborum. Sed ut perspiciatis unde omnis iste natus error sit voluptatem accusantium doloremque laudantium, totam rem aperiam, eaque ipsa quae ab illo inventore veritatis et quasi architecto beatae vitae dicta sunt explicabo. Nemo enim ipsam voluptatem quia voluptas sit aspernatur aut odit aut fugit, sed quia consequuntur magni dolores eos qui ratione voluptatem sequi nesciunt. Neque porro quisquam est, qui dolorem ipsum quia dolor sit amet, consectetur, adipisci velit, sed quia non numquam eius modi tempora incidunt ut labore et dolore magnam aliquam quaerat voluptatem.</p>
      <p>Lorem ipsum dolor sit amet, consectetur adipisicing elit, sed do eiusmod tempor incididunt ut labore et dolore magna aliqua. Ut enim ad minim veniam, quis nostrud exercitation ullamco laboris nisi ut aliquip ex ea commodo consequat. Duis aute irure dolor in reprehenderit in voluptate velit esse cillum dolore eu fugiat nulla pariatur. Excepteur sint occaecat cupidatat non proident, sunt in culpa qui officia deserunt mollit anim id est laborum. Sed ut perspiciatis unde omnis iste natus error sit voluptatem accusantium doloremque laudantium, totam rem aperiam, eaque ipsa quae ab illo inventore veritatis et quasi architecto beatae vitae dicta sunt explicabo. Nemo enim ipsam voluptatem quia voluptas sit aspernatur aut odit aut fugit, sed quia consequuntur magni dolores eos qui ratione voluptatem sequi nesciunt. Neque porro quisquam est, qui dolorem ipsum quia dolor sit amet, consectetur, adipisci velit, sed quia non numquam eius modi tempora incidunt ut labore et dolore magnam aliquam quaerat voluptatem.</p>
    </div>
    <div class="isbn-box"></div>
  </section>

  <!-- Spine -->
  <section class="spine">
    <svg class="spine-title title-svg" viewBox="0 0 76 360" aria-label="Find Your Mentor">
      <g transform="translate(8,0) rotate(90)">
        <text class="display" x="4" y="0" font-size="84" textLength="140" lengthAdjust="spacingAndGlyphs">FIND</text>
        <text class="serif your" x="152" y="-18" font-size="30" textLength="84" lengthAdjust="spacingAndGlyphs">YOUR</text>
        <text class="display" x="244" y="0" font-size="84" textLength="112" lengthAdjust="spacingAndGlyphs">MENTOR</text>
      </g>
    </svg>
    <svg class="spine-author" viewBox="0 0 50 225" aria-label="Author's Name">
      <g transform="translate(6,0) rotate(90)">
        <text x="2" y="0" font-size="44" textLength="220" lengthAdjust="spacingAndGlyphs">AUTHOR’S NAME</text>
      </g>
    </svg>
  </section>

  <!-- Front cover -->
  <section class="front-cover">
    <svg class="front-title title-svg" viewBox="0 0 530 500" aria-label="Find Your Mentor">
      <path class="cape-art" role="img" aria-label="Red superhero cape draped over the title"
        fill="var(--cape)" d="M42 260 C10 300 -5 380 40 440 C70 480 110 490 135 478 L140 300 C150 285 185 272 230 280 C300 290 350 320 365 360 L360 410 C320 400 250 400 210 408 L140 300 Z"/>
      <text class="display" x="50" y="212" font-size="286" textLength="455" lengthAdjust="spacingAndGlyphs">FIND</text>
      <text class="serif your" x="190" y="259" font-size="48" textLength="140" lengthAdjust="spacingAndGlyphs">YOUR</text>
      <text class="display" x="50" y="503" font-size="340" textLength="455" lengthAdjust="spacingAndGlyphs">MENTOR</text>
    </svg>

    <div class="rule rule--top"></div>
    <svg class="subtitle" viewBox="0 0 465 80" aria-label="How to accelerate your growth through reaching out, getting a response from, and leaving an impression on the people you admire most">
      <text x="55" y="22" textLength="335" lengthAdjust="spacingAndGlyphs">HOW TO ACCELERATE YOUR GROWTH THROUGH</text>
      <text x="12" y="46" textLength="441" lengthAdjust="spacingAndGlyphs">REACHING OUT, GETTING A RESPONSE FROM, AND LEAVING AN</text>
      <text x="63" y="70" textLength="340" lengthAdjust="spacingAndGlyphs">IMPRESSION ON THE PEOPLE YOU ADMIRE MOST</text>
    </svg>
    <div class="rule rule--bottom"></div>

    <svg class="front-author" viewBox="0 0 280 56" aria-label="Author's Name">
      <text x="6" y="50" font-size="60" textLength="268" lengthAdjust="spacingAndGlyphs">AUTHOR’S NAME</text>
    </svg>
  </section>

</main>
</body>
</html>
```